Business card design and logo needed - Photographer

I take photos of weddings, rodeos, snowmobiling.
Need a card to hand out to prospective clients.
Industry/Entity Type
Business
Contact Information for Business Card
Marcus Dolven Photography
Requirements
Must have
- Bold
Black or white base.
My website. www.MarcusDolven.example
Should not have
- camera/ lens/ aperture blades

```html
<!DOCTYPE html>
<html lang="en">
<head>
<meta charset="utf-8">
<title>Marcus Dolven Photography – Business Card</title>
<link rel="stylesheet" href="https://fonts.googleapis.com/css2?family=Quicksand:wght@500;600&display=swap">
<style>
  :root {
    --page-bg: #3b4142;
    --card-base: #1f2929;
    --card-edge: #141b1b;
    --band-left: #152020;
    --band-right-start: #162121;
    --band-right-end: #1c2828;
    --divider: #0f1616;
    --text-light: #e6ecec;
    --brand-blue: #5aa8e8;
  }
  html, body {
    margin: 0;
    padding: 0;
    width: 1200px;
    height: 1000px;
    overflow: hidden;
    background: var(--page-bg);
  }
  .canvas {
    position: relative;
    width: 1200px;
    height: 1000px;
  }
  .business-card {
    position: absolute;
    left: 194px;
    top: 248px;
    width: 810px;
    height: 450px;
    font-family: "Quicksand", sans-serif;
    color: var(--text-light);
  }
  .card-shape {
    position: absolute;
    inset: 0;
  }
  .brand {
    position: absolute;
    left: 0;
    right: 0;
    top: 88px;
    display: flex;
    align-items: center;
    justify-content: center;
    gap: 16px;
  }
  .brand-dot {
    width: 26px;
    height: 26px;
    border-radius: 50%;
    background: var(--brand-blue);
  }
  .brand-name {
    font-size: 30px;
    font-weight: 600;
    letter-spacing: 2px;
    color: var(--brand-blue);
  }
  .holder-name {
    position: absolute;
    left: 0;
    width: 401px;
    top: 284px;
    text-align: center;
    font-size: 38px;
    font-weight: 500;
    margin: 0;
  }
  .contact-list {
    position: absolute;
    right: 25px;
    top: 262px;
    margin: 0;
    padding: 0;
    list-style: none;
    text-align: right;
    font-size: 23px;
    font-weight: 500;
    line-height: 32px;
  }
  .contact-phone {
    margin-top: 8px;
  }
</style>
</head>
<body>
<main class="canvas">
  <section class="business-card" aria-label="Business card for Marcus Dolven Photography">
    <svg class="card-shape" width="810" height="450" viewBox="0 0 810 450" aria-hidden="true">
      <defs>
        <linearGradient id="bandRight" x1="0" y1="0" x2="1" y2="0">
          <stop offset="0" stop-color="var(--band-right-start)"/>
          <stop offset="1" stop-color="var(--band-right-end)"/>
        </linearGradient>
      </defs>
      <path d="M0,0 H782 Q810,0 810,28 V450 H28 Q0,450 0,422 Z" fill="var(--card-base)"/>
      <polygon points="0,0 440,0 426,10 0,10" fill="var(--card-edge)"/>
      <polygon points="384,440 810,440 810,450 370,450" fill="var(--card-edge)"/>
      <rect x="0" y="244" width="401" height="138" fill="var(--band-left)"/>
      <rect x="401" y="244" width="3" height="138" fill="var(--divider)"/>
      <rect x="404" y="244" width="406" height="138" fill="url(#bandRight)"/>
    </svg>

    <div class="brand">
      <span class="brand-dot"></span>
      <span class="brand-name">Marcus Dolven Photography</span>
    </div>

    <h1 class="holder-name">Marcus Dolven</h1>

    <ul class="contact-list">
      <li class="contact-email">marcusdolven@mail.example</li>
      <li class="contact-web">www.MarcusDolven.example</li>
      <li class="contact-phone">306 555 0142</li>
    </ul>
  </section>
</main>
</body>
</html>
```